Business Card Design Project

Attached is a rough business card design. We like this general design but we feel that the layout, text, color can use improvement and we seek the help of a professional designer.
We have a television and film production company based in New York. We need our cards for television network executives, other production executives, financiers etc. We deal with creative types as well as business people so we need the card to be interesting and edgy just like the name of our company - KICKTHEDOOR. The design should reflect the edgy, punk rock attitude of our company.
We prefer orange typeface for the logo but we're open to other ideas. I am attaching our existing business card and other files to help with the design.
Thank you in advance!!
Updates
Target Market(s)
Television and film producers, television network executives, other production executives, financiers, distribution companies
Industry/Entity Type
Film Production
Requirements
Must have
- I am attaching a photo of the company mascot which is a dog. We prefer to have the dog's photo as part of the card but we're open to the other ideas.
Name, phone number, email

```html
<!DOCTYPE html>
<html lang="en">
<head>
<meta charset="utf-8">
<title>KICKTHEDOOR – Business Card</title>
<link href="https://fonts.googleapis.com/css2?family=Questrial&display=swap" rel="stylesheet">
<style>
  :root {
    --page-bg: #d9d9d9;
    --card-bg: #2a2828;
    --card-edge: #1f1d1d;
    --text-light: #f4f4f4;
    --photo-light: #e6e6e6;
    --photo-mid: #9a9a9a;
    --photo-dark: #3a3a3a;
  }
  * { margin: 0; padding: 0; box-sizing: border-box; }
  html, body {
    width: 1200px;
    height: 768px;
    overflow: hidden;
    background: var(--page-bg);
    font-family: "Questrial", "Century Gothic", sans-serif;
  }
  .business-card {
    position: absolute;
    left: 60px;
    top: 77px;
    width: 1080px;
    height: 614px;
    background: linear-gradient(160deg, #312f2f 0%, var(--card-bg) 55%, var(--card-edge) 100%);
    overflow: hidden;
  }
  .mascot-photo {
    position: absolute;
    left: 532px;
    top: 0;
    width: 548px;
    height: 420px;
    border-bottom-left-radius: 90px 120px;
    background: radial-gradient(ellipse at 65% 35%, var(--photo-light) 0%, var(--photo-mid) 50%, var(--photo-dark) 100%);
  }
  .contact-name {
    position: absolute;
    left: 70px;
    top: 176px;
    font-size: 37px;
    color: var(--text-light);
    letter-spacing: 0.2px;
  }
  .contact-list {
    position: absolute;
    left: 70px;
    top: 284px;
    list-style: none;
    color: var(--text-light);
    font-size: 28px;
  }
  .contact-list li {
    display: flex;
    align-items: center;
    gap: 10px;
    height: 43px;
  }
  .contact-icon {
    width: 20px;
    height: 20px;
    fill: var(--text-light);
  }
  .company-name {
    position: absolute;
    left: 70px;
    top: 430px;
    font-size: 150px;
    line-height: 1;
    color: var(--text-light);
    letter-spacing: 4px;
  }
</style>
</head>
<body>
  <div class="business-card">
    <div class="mascot-photo" role="img" aria-label="Black and white photo of the company mascot, a bulldog resting its head"></div>

    <p class="contact-name">Marcus Delaney</p>

    <ul class="contact-list">
      <li>
        <svg class="contact-icon" viewBox="0 0 20 20" aria-hidden="true">
          <path d="M5 2 L8 2 L9 6 L7 8 C8 10.5 9.5 12 12 13 L14 11 L18 12 L18 15 C18 16.5 17 18 15 18 C8 17.5 2.5 12 2 5 C2 3 3.5 2 5 2 Z"/>
        </svg>
        <span>917-555-0148</span>
      </li>
      <li>
        <svg class="contact-icon" viewBox="0 0 20 20" aria-hidden="true">
          <path d="M2 5 L18 5 L18 16 L2 16 Z M3.5 6.5 L10 11 L16.5 6.5" fill="none" stroke="#f4f4f4" stroke-width="1.6"/>
        </svg>
        <span>Marcus@kickthedoor.com</span>
      </li>
    </ul>

    <p class="company-name">kickthedoor</p>
  </div>
</body>
</html>
```